First Aid Training business needs business card design

We would like a double sided business card designed for a first aid training business - Brindlewood First Aid. We provide first aid training and , WHS (work, health and safety) training.

The attached word document contains the key information we would like on each side of the business card.

Final design needs to be delivered in print ready format, along with the original file.

```html
<!DOCTYPE html>
<html lang="en">
<head>
<meta charset="utf-8">
<title>Brindlewood First Aid – Business Card</title>
<link href="https://fonts.googleapis.com/css2?family=Montserrat:wght@600&family=Source+Sans+3:wght@400;700&display=swap" rel="stylesheet">
<style>
  :root {
    --red: #ed2224;
    --white: #ffffff;
    --ink: #111111;
    --page: #ffffff;
  }
  * { box-sizing: border-box; margin: 0; padding: 0; }
  html, body { width: 1200px; height: 900px; overflow: hidden; background: var(--page); }
  .sheet { position: relative; width: 1200px; height: 900px; }

  .card {
    position: absolute;
    left: 263px;
    width: 675px;
    height: 405px;
    background: var(--white);
    overflow: hidden;
    box-shadow: -4px 6px 10px rgba(0,0,0,0.25);
  }
  .card--front { top: 28px; }
  .card--back { top: 467px; }
  .card__shape { position: absolute; inset: 0; }

  /* Front */
  .brand-block {
    position: absolute;
    left: 40px; top: 95px;
    width: 280px;
    display: flex; flex-direction: column; align-items: center;
    font-family: "Montserrat", sans-serif; font-weight: 600; color: var(--ink);
  }
  .brand-block__dot {
    width: 96px; height: 96px; border-radius: 50%;
    background: var(--red); margin-bottom: 22px;
  }
  .brand-block__name { font-size: 30px; letter-spacing: 0.5px; line-height: 1; }
  .brand-block__tag { font-size: 18px; margin-top: 8px; line-height: 1; }

  .contact { position: absolute; left: 368px; top: 0; color: var(--white); font-family: "Source Sans 3", sans-serif; }
  .contact__person { position: absolute; top: 128px; left: 0; display: flex; align-items: center; gap: 14px; white-space: nowrap; }
  .contact__person-name { font-weight: 700; font-size: 25px; letter-spacing: 0.3px; }
  .contact__row { position: absolute; left: 0; display: flex; align-items: center; gap: 12px; white-space: nowrap; font-size: 16.5px; }
  .contact__row--phone { top: 200px; }
  .contact__row--mail { top: 237px; }
  .contact__row--web { top: 275px; }
  .contact__icon {
    width: 28px; height: 30px; border-radius: 5px; background: var(--white);
    display: flex; align-items: center; justify-content: center; flex: none;
  }

  /* Back */
  .lockup {
    position: absolute; left: 254px; top: 56px;
    display: flex; align-items: center; gap: 16px;
    font-family: "Montserrat", sans-serif; font-weight: 600; color: var(--white);
  }
  .lockup__dot { width: 56px; height: 56px; border-radius: 50%; background: var(--white); flex: none; }
  .lockup__name { font-size: 22px; line-height: 1; }
  .lockup__tag { font-size: 11px; line-height: 1; margin-top: 5px; }

  .pitch {
    position: absolute; left: 0; right: 0; top: 208px;
    text-align: center; color: var(--red);
    font-family: "Source Sans 3", sans-serif; font-weight: 700; font-size: 25px;
  }
  .benefits { position: absolute; left: 188px; top: 251px; width: 300px; list-style: none; }
  .benefits__item {
    height: 22px; margin-bottom: 3.5px; border-radius: 5px; background: var(--red);
    color: var(--white); font-family: "Source Sans 3", sans-serif; font-size: 17px;
    line-height: 22px; text-align: center; white-space: nowrap;
  }
</style>
</head>
<body>
<main class="sheet">

  <section class="card card--front" aria-label="Business card front">
    <svg class="card__shape" width="675" height="405" viewBox="0 0 675 405" aria-hidden="true">
      <circle cx="571" cy="203" r="234" fill="var(--red)"/>
    </svg>

    <div class="brand-block">
      <span class="brand-block__dot"></span>
      <span class="brand-block__name">BRINDLEWOOD</span>
      <span class="brand-block__tag">FIRST AID TRAINING</span>
    </div>

    <div class="contact">
      <div class="contact__person">
        <svg width="28" height="34" viewBox="0 0 28 34" aria-hidden="true">
          <circle cx="14" cy="9" r="8" fill="var(--white)"/>
          <path d="M0 34 V26 Q0 18 8 18 H20 Q28 18 28 26 V34 Z" fill="var(--white)"/>
        </svg>
        <span class="contact__person-name">DANA MARLOWE</span>
      </div>
      <div class="contact__row contact__row--phone">
        <span class="contact__icon">
          <svg width="18" height="18" viewBox="0 0 24 24" aria-hidden="true"><path fill="var(--red)" d="M6.6 10.8a15.1 15.1 0 0 0 6.6 6.6l2.2-2.2c.3-.3.7-.4 1-.2 1.1.4 2.3.6 3.6.6.6 0 1 .4 1 1V20c0 .6-.4 1-1 1A17 17 0 0 1 3 4c0-.6.4-1 1-1h3.5c.6 0 1 .4 1 1 0 1.3.2 2.5.6 3.6.1.3 0 .7-.2 1z"/></svg>
        </span>
        <span>0491 570 226</span>
      </div>
      <div class="contact__row contact__row--mail">
        <span class="contact__icon">
          <svg width="16" height="12" viewBox="0 0 16 12" aria-hidden="true"><rect x="0.75" y="0.75" width="14.5" height="10.5" fill="none" stroke="var(--red)" stroke-width="1.5"/><path d="M1 1 L8 7 L15 1 M1 11 L6 5.5 M15 11 L10 5.5" fill="none" stroke="var(--red)" stroke-width="1.3"/></svg>
        </span>
        <span>help@brindlewoodfirstaid.com.au</span>
      </div>
      <div class="contact__row contact__row--web">
        <span class="contact__icon">
          <svg width="14" height="18" viewBox="0 0 14 18" aria-hidden="true"><path fill="var(--red)" d="M7 0a7 7 0 0 0-7 7c0 5 7 11 7 11s7-6 7-11a7 7 0 0 0-7-7zm0 9.5A2.5 2.5 0 1 1 7 4.5a2.5 2.5 0 0 1 0 5z"/></svg>
        </span>
        <span>www.brindlewoodfirstaid.com.au</span>
      </div>
    </div>
  </section>

  <section class="card card--back" aria-label="Business card back">
    <svg class="card__shape" width="675" height="405" viewBox="0 0 675 405" aria-hidden="true">
      <path d="M0 0 H675 V51 Q337.5 233 0 51 Z" fill="var(--red)"/>
    </svg>

    <div class="lockup">
      <span class="lockup__dot"></span>
      <div>
        <div class="lockup__name">BRINDLEWOOD</div>
        <div class="lockup__tag">FIRST AID TRAINING</div>
      </div>
    </div>

    <p class="pitch">ONSITE TRAINING – WE CAN COME TO YOU</p>
    <ul class="benefits">
      <li class="benefits__item">TIME EFFICIENT</li>
      <li class="benefits__item">COST EFFECTIVE</li>
      <li class="benefits__item">MINIMISE DOWNTIME FOR YOUR TEAM</li>
    </ul>
  </section>

</main>
</body>
</html>
```